Design a cover for a book called The Quiet Harvest

Describe a cover for a 5.5" x 8.5" 200-page paperback book titled The Quiet Harvest. The subtitle is: A Practical Handbook for Shaping a Country Where Every Person Can Thrive

The book is about how we can change our economic system to provide universal basic income, free healthcare, and free college while also lowering our tax rates. The book is uplifting, talks about the spiritual growth our society will need in positive terms. The website ThePublicPlentyPlan.example will be used to promote the book, and is a good resources for design ideas.

Target Market(s)

Economics, Finance, Spiritual

Font styles to use
Serif
Sans Serif

Colors

Designer to choose colors to be used in the design.

Requirements
Must have
• Include the URL on the back cover: TheQuietHarvest.example
Include the attached ISBN Barcode on the back cover
Include the title on the front cover: The Quiet Harvest
Include the subtitle on the front cover: A Practical Handbook for Shaping a Country Where Every Person Can Thrive
Include the author's name Neil Barnaby Holt on the front cover

Here is the size of the cover:
Spine Width 0.4504” (200 x 0.002252”)
Full Width 11.7004” (0.125 + 5.5 + 0.4504 + 5.5 +0.125) 3511 pixels @300DPI
Full Height 8.75” (0.125 + 8.5 + 0.125) 2625 pixels @ 300DPI

```html
<!DOCTYPE html>
<html lang="en">
<head>
<meta charset="utf-8">
<title>The Quiet Harvest — Cover Wrap</title>
<link href="https://fonts.googleapis.com/css2?family=Bebas+Neue&family=Montserrat:wght@400;500&family=Open+Sans:wght@400&display=swap" rel="stylesheet">
<style>
  :root {
    --stage: #e4e4e4;
    --paper: #f3f3f3;
    --paper-back: #ececec;
    --purple: #4a2c72;
    --gold: #e9aa4f;
    --ink: #3a3a3a;
    --sketch-light: #f0f0f0;
    --sketch-dark: #c9c9c9;
  }
  * { box-sizing: border-box; margin: 0; padding: 0; }
  html, body { width: 1200px; height: 857px; overflow: hidden; background: var(--stage); }
  .wrap {
    position: absolute; left: 128px; top: 78px;
    width: 943px; height: 700px;
    display: flex;
    box-shadow: 0 6px 24px rgba(0,0,0,0.12);
  }
  .back-cover { width: 453px; height: 700px; background: var(--paper-back); position: relative; }
  .spine { width: 37px; height: 700px; background: var(--paper); position: relative; border-left: 1px solid #dcdcdc; border-right: 1px solid #dcdcdc; }
  .front-cover { width: 453px; height: 700px; background: var(--paper); position: relative; }

  .title { font-family: "Bebas Neue", sans-serif; font-weight: 400; text-align: center; line-height: 0.86; }
  .title .the { color: var(--purple); display: block; }
  .title .main { color: var(--gold); display: block; }

  /* Front */
  .front-cover .title { position: absolute; top: 64px; left: 0; right: 0; }
  .front-cover .title .the { font-size: 64px; }
  .front-cover .title .main { font-size: 124px; }
  .subtitle {
    position: absolute; top: 410px; left: 40px; right: 40px; text-align: center;
    font-family: "Montserrat", sans-serif; font-weight: 500; font-size: 15px; line-height: 1.35;
    color: var(--purple);
  }
  .cover-art {
    position: absolute; left: 70px; top: 468px; width: 313px; height: 135px;
    background: radial-gradient(ellipse at 50% 45%, var(--sketch-dark) 0%, var(--sketch-light) 70%);
    border-radius: 6px;
  }
  .front-cover .author {
    position: absolute; bottom: 30px; left: 0; right: 0; text-align: center;
    font-family: "Bebas Neue", sans-serif; font-size: 58px; color: var(--purple); line-height: 1;
  }

  /* Spine */
  .spine-text {
    position: absolute; left: 50%; transform: translateX(-50%);
    writing-mode: vertical-rl; font-family: "Bebas Neue", sans-serif; font-size: 24px; line-height: 1; white-space: nowrap;
  }
  .spine-title { top: 30px; }
  .spine-title .the { color: var(--purple); }
  .spine-title .main { color: var(--gold); }
  .spine-author { bottom: 30px; color: var(--purple); }

  /* Back */
  .back-cover .title { position: absolute; top: 44px; left: 0; right: 0; }
  .back-cover .title .the { font-size: 34px; }
  .back-cover .title .main { font-size: 48px; }
  .blurb {
    position: absolute; top: 184px; left: 42px; right: 42px;
    font-family: "Open Sans", sans-serif; font-size: 11.5px; line-height: 1.4; color: var(--ink);
  }
  .blurb p + p { margin-top: 11px; }
  .author-heading {
    position: absolute; top: 502px; left: 0; right: 0; text-align: center;
    font-family: "Bebas Neue", sans-serif; font-weight: 400; font-size: 28px; line-height: 1; color: var(--purple);
  }
  .author-photo {
    position: absolute; top: 540px; left: 42px; width: 70px; height: 96px;
    background: linear-gradient(160deg, #8a7358 0%, #c89a78 55%, #6b3b34 100%);
  }
  .author-bio {
    position: absolute; top: 538px; left: 124px; right: 42px;
    font-family: "Open Sans", sans-serif; font-size: 11px; line-height: 1.25; color: #222;
  }
  .site-url {
    position: absolute; bottom: 26px; left: 0; right: 0; text-align: center;
    font-family: "Montserrat", sans-serif; font-weight: 500; font-size: 14px; color: var(--purple);
  }
</style>
</head>
<body>
  <div class="wrap">
    <section class="back-cover">
      <h2 class="title"><span class="the">The</span><span class="main">Quiet<br>Harvest</span></h2>
      <div class="blurb">
        <p>Lorem ipsum dolor sit amet, consectetur adipisicing elit, sed do eiusmod tempor incididunt ut labore et dolore magna aliqua. Ut enim ad minim veniam, quis nostrud exercitation ullamco laboris nisi ut aliquip ex ea commodo consequat.</p>
        <p>Duis aute irure dolor in reprehenderit in voluptate velit esse cillum dolore eu fugiat nulla pariatur. Excepteur sint occaecat cupidatat non proident, sunt in culpa qui officia deserunt mollit anim id est laborum. Sed ut perspiciatis unde omnis iste natus error sit voluptatem accusantium doloremque laudantium, totam rem aperiam, eaque ipsa quae ab illo inventore veritatis et quasi architecto beatae vitae dicta sunt explicabo.</p>
        <p>Nemo enim ipsam voluptatem quia voluptas sit aspernatur aut odit aut fugit, sed quia consequuntur magni dolores eos qui ratione voluptatem sequi nesciunt. Neque porro quisquam est, qui dolorem ipsum quia dolor sit amet, consectetur, adipisci velit, sed quia non numquam eius modi tempora incidunt ut labore et dolore magnam aliquam quaerat voluptatem.</p>
      </div>
      <h3 class="author-heading">Neil Barnaby Holt</h3>
      <div class="author-photo" role="img" aria-label="Portrait photograph of the author"></div>
      <p class="author-bio">Neil Barnaby Holt is the author of The Open Ledger for the Common Economy. As a citizen concerned about our nation's future, he embarked on a mission to find a nonpartisan solution to poverty, Social Security, the decline of our middle class, our deficit, our skyrocketing national debt, and the high cost of taxes, healthcare, and college.</p>
      <p class="site-url">TheQuietHarvest.example</p>
    </section>

    <section class="spine">
      <div class="spine-text spine-title"><span class="the">The</span> <span class="main">Quiet Harvest</span></div>
      <div class="spine-text spine-author">Neil Barnaby Holt</div>
    </section>

    <section class="front-cover">
      <h1 class="title"><span class="the">The</span><span class="main">Quiet<br>Harvest</span></h1>
      <p class="subtitle">A Practical Handbook for Shaping a Country Where Every Person Can Thrive</p>
      <div class="cover-art" role="img" aria-label="Pencil sketch of business people floating through the sky holding bunches of dollar-sign balloons among small clouds and birds"></div>
      <p class="author">Neil Barnaby Holt</p>
    </section>
  </div>
</body>
</html>
```